Website Design for Employee Moral and Happiness Company

Looking for a clean website design that explains our features in a step by step manner so our visitors know exactly what our site does before logging in.

The site is called "Velquo". See logo design and video for a sample of style and an overview of what we do.

Target Market(s)

Business owners that are looking to retain employees.

Number of Pages Required

1 page

```html
<!DOCTYPE html>
<html lang="en">
<head>
<meta charset="utf-8">
<title>Velquo – Employee Morale and Happiness</title>
<link href="https://fonts.googleapis.com/css2?family=Playfair+Display:wght@500;600;700&family=Poppins:wght@400;500;600&display=swap" rel="stylesheet">
<style>
:root{
  --orange:#f0501a;
  --blue:#4a86f0;
  --ink:#222222;
  --muted:#444444;
  --soft:#f2f3f5;
  --line:#d9d9d9;
  --white:#ffffff;
}
*{box-sizing:border-box;margin:0;padding:0}
html,body{width:1200px;height:3578px;overflow:hidden;background:var(--white)}
body{font-family:'Poppins',sans-serif;color:var(--ink);position:relative}
.page{position:relative;width:1200px;height:3578px;overflow:hidden}
.abs{position:absolute}
.serif{font-family:'Playfair Display',serif}

/* header */
.brand{left:40px;top:14px;font-family:'Playfair Display',serif;font-weight:700;font-size:44px;color:var(--ink);letter-spacing:1px}
.nav{top:33px;left:340px;display:flex;gap:0;font-size:15px;color:var(--ink)}
.nav a{position:absolute;white-space:nowrap;text-decoration:none;color:var(--ink)}
.login{left:885px;top:32px;font-size:15px;font-weight:500;display:flex;align-items:center;gap:8px}
.callbar{left:971px;top:18px;width:194px;height:48px}
.callbar span{position:absolute;left:42px;top:13px;color:var(--white);font-size:15px;font-weight:600}

/* hero */
.hero{left:0;top:86px;width:1200px;height:640px}
.hero-box{left:61px;top:210px;width:542px;height:262px;background:rgba(255,255,255,.75);box-shadow:0 0 0 12px rgba(255,255,255,.35)}
.hero-title{left:107px;top:250px;font-family:'Playfair Display',serif;font-weight:600;font-size:43px;color:var(--orange);white-space:nowrap}
.hero-title b{color:var(--blue);font-weight:600}
.hero-sub{left:111px;top:314px;font-size:15.5px;font-weight:500;line-height:25px;color:var(--ink)}
.btn{display:flex;align-items:center;color:var(--white);font-size:15px;font-weight:600;height:47px;padding-left:31px;background:var(--orange);clip-path:polygon(0 0,100% 0,86% 100%,0 100%);box-shadow:4px 5px 10px rgba(0,0,0,.15)}
.dot{width:13px;height:13px;border-radius:50%;left:1137px}

/* headings */
.h2{font-family:'Playfair Display',serif;font-weight:600;font-size:30px;color:var(--orange);white-space:nowrap}
.h2 b{color:var(--blue);font-weight:600}

/* about */
.mascot{left:110px;top:795px;width:475px;height:345px;display:flex;align-items:center;justify-content:center;gap:22px}
.mascot span{font-family:'Playfair Display',serif;font-weight:700;font-size:86px;color:var(--blue)}
.about-text{left:644px;top:864px;width:413px;font-size:15px;line-height:25.7px;text-align:justify;color:var(--ink)}

/* features */
.features{left:0;top:1230px;width:1200px;height:682px;background:var(--soft);border-radius:0 50px 0 40px}
.feature{width:224px;height:242px;padding:18px 0 0 28px}
.feature.active{border:2px solid var(--orange)}
.ficon{width:62px;height:62px;border-radius:10px}
.feature h3{font-family:'Playfair Display',serif;font-weight:500;font-size:21px;margin-top:22px;white-space:nowrap}
.feature p{font-size:15px;line-height:26px;margin-top:6px}
.feature a{display:inline-block;color:var(--orange);font-size:15px;font-weight:500;margin-top:10px;border-bottom:1px solid var(--orange);text-decoration:none;line-height:20px}
.video{left:600px;top:1315px;width:620px;height:595px;background:var(--orange);border-radius:80px 0 0 70px}
.video-art{left:620px;top:1315px;width:600px;height:577px;border-radius:72px 0 0 60px;background:linear-gradient(160deg,#1f3a66 0%,#2fa3a0 38%,#e9e2d8 62%,#a69e95 100%)}

/* testimonial */
.t-card{left:308px;top:2095px;width:584px;height:320px;background:var(--white);box-shadow:0 3px 14px rgba(0,0,0,.16)}
.t-text{left:338px;top:2175px;width:524px;font-size:15px;line-height:25.7px;text-align:center}
.t-divider{left:308px;top:2320px;width:584px;height:1px;background:var(--line)}
.t-name{left:308px;top:2338px;width:584px;text-align:center;font-family:'Playfair Display',serif;font-size:19px}
.t-name small{font-family:'Poppins',sans-serif;font-size:15px}
.stars{left:308px;top:2366px;width:584px;text-align:center;color:#f5b300;font-size:18px;letter-spacing:2px}
.quote{font-family:'Playfair Display',serif;font-size:96px;color:#c9c9c9;line-height:1;top:2322px}
.avatar{border-radius:50%;box-shadow:0 3px 10px rgba(0,0,0,.2)}

/* blog */
.blog{left:0;top:2505px;width:1200px;height:700px;background:var(--soft)}
.post{width:309px;height:410px;background:var(--white);border:1px solid #cfcfcf;top:2655px}
.post .img{position:absolute;left:5px;top:5px;width:297px;height:230px}
.post .date{position:absolute;top:216px;left:50%;transform:translateX(-50%);background:var(--orange);color:var(--white);font-size:15px;font-weight:500;padding:2px 14px}
.post h4{position:absolute;top:255px;left:0;width:100%;text-align:center;font-family:'Playfair Display',serif;font-weight:600;font-size:19px}
.post p{position:absolute;top:290px;left:20px;width:267px;text-align:center;font-size:15px;line-height:25.7px}

/* footer */
.footer-name{left:105px;top:3318px;font-family:'Playfair Display',serif;font-weight:700;font-size:60px;color:var(--white);letter-spacing:2px}
.fhead{top:3288px;font-family:'Playfair Display',serif;font-weight:500;font-size:20px;color:var(--white);white-space:nowrap}
.flinks{left:438px;top:3323px;font-size:15px;line-height:24.3px;color:var(--white)}
.email{left:624px;top:3330px;width:273px;height:41px;background:var(--white);font-size:14px;color:#b5b5b5;padding:12px 12px}
.social{width:34px;height:34px;border-radius:50%;background:var(--white);top:3326px}
.fline{left:140px;top:3505px;width:950px;height:1px;background:rgba(255,255,255,.6)}
.copy{left:0;top:3529px;width:1200px;text-align:center;font-size:15px;color:var(--white)}
</style>
</head>
<body>
<div class="page">

  <!-- header -->
  <div class="abs brand">velquo</div>
  <nav class="abs nav" style="left:0;top:33px">
    <a style="left:340px">Home</a>
    <a style="left:411px">About</a>
    <a style="left:481px">Our Feature ⌄</a>
    <a style="left:593px">Testimonial</a>
    <a style="left:703px">Blog</a>
    <a style="left:763px">Contact</a>
  </nav>
  <svg class="abs" style="left:833px;top:31px" width="22" height="22" viewBox="0 0 22 22"><circle cx="9" cy="9" r="7" fill="none" stroke="#222" stroke-width="2.2"/><line x1="14" y1="14" x2="20" y2="20" stroke="#222" stroke-width="2.5"/></svg>
  <div class="abs" style="left:870px;top:28px;width:2px;height:28px;background:#222"></div>
  <div class="abs login">
    <svg width="16" height="18" viewBox="0 0 16 18"><circle cx="8" cy="5" r="4" fill="none" stroke="#f0501a" stroke-width="1.6"/><path d="M1 17c0-4 3-6 7-6s7 2 7 6" fill="none" stroke="#f0501a" stroke-width="1.6"/></svg>
    LOGIN
  </div>
  <div class="abs callbar">
    <svg class="abs" style="left:0;top:0" width="194" height="48" viewBox="0 0 194 48"><rect width="40" height="48" fill="#4a86f0"/><polygon points="40,0 194,0 180,48 40,48" fill="#f0501a"/><path d="M13 15c0 10 7 18 16 19l3-4-4-3-2 2c-4-2-6-5-8-9l2-2-3-4z" fill="#fff"/></svg>
    <span>+1(555) 010 4477</span>
  </div>

  <!-- hero -->
  <svg class="abs hero" viewBox="0 0 1200 640" role="img" aria-label="Photo of a smiling businesswoman at her laptop in a bright office">
    <defs>
      <linearGradient id="heroBg" x1="0" y1="0" x2="1" y2="0">
        <stop offset="0" stop-color="#d9d8d6"/><stop offset=".45" stop-color="#eeecea"/>
        <stop offset=".7" stop-color="#8a6a58"/><stop offset="1" stop-color="#c9c5c2"/>
      </linearGradient>
    </defs>
    <path d="M0 0H1200V600C1050 640 900 640 760 630C560 615 420 545 240 550C130 553 50 580 0 600Z" fill="url(#heroBg)"/>
    <path d="M0 600C50 580 130 553 240 550C420 545 560 615 760 630C900 640 1050 640 1200 600V625C1050 645 900 648 760 640C560 625 420 565 240 570C130 573 50 598 0 614Z" fill="#f0501a"/>
  </svg>
  <div class="abs hero-box"></div>
  <div class="abs hero-title">Welcome to the <b>Velquo</b></div>
  <div class="abs hero-sub">Nemo Enim Ipsam Voluptatem Quia Voluptas<br>Sit Aspernatur Aut Odit Aut Fugit, Sed Quia</div>
  <div class="abs btn" style="left:112px;top:383px;width:172px">GET STARTED</div>
  <div class="abs dot" style="top:326px;background:#d0d0d0"></div>
  <div class="abs dot" style="top:350px;background:#7a7a7a"></div>
  <div class="abs dot" style="top:374px;background:var(--orange)"></div>

  <!-- about -->
  <div class="abs mascot">
    <svg width="90" height="90" viewBox="0 0 90 90"><circle cx="45" cy="45" r="44" fill="#4a86f0"/></svg>
    <span>Velquo</span>
  </div>
  <div class="abs h2" style="left:644px;top:800px">ABOUT <b>US</b></div>
  <svg class="abs" style="left:644px;top:840px" width="56" height="14" viewBox="0 0 56 14"><path d="M3 3Q28 20 53 3" fill="none" stroke="#f0501a" stroke-width="2.5" stroke-linecap="round"/></svg>
  <p class="abs about-text">Ut Enim Ad Minima Veniam, Quis Nostrum Exercitationem Ullam Corporis Suscipit Laboriosam, Nisi Ut Aliquid Ex Ea Commodi Consequatur? Quis Autem Vel Eum Iure Reprehenderit Qui In Ea Voluptate Velit Esse Quam Nihil Molestiae Consequatur, Vel Illum Qui Dolorem Eum Fugiat Quo Voluptas Nulla Pariaturlorem Ipsum Dolor Sit Amet, Consectetur Adipiscing Elit, Sed Do Eiusmod Tempor Incididunt Ut</p>
  <div class="abs btn" style="left:646px;top:1090px;width:172px">READ MORE</div>

  <!-- features -->
  <div class="abs features"></div>
  <div class="abs h2" style="left:47px;top:1300px">OUR <b>FEATURES</b></div>
  <svg class="abs" style="left:47px;top:1340px" width="56" height="14" viewBox="0 0 56 14"><path d="M3 3Q28 20 53 3" fill="none" stroke="#f0501a" stroke-width="2.5" stroke-linecap="round"/></svg>

  <div class="abs feature active" style="left:50px;top:1368px">
    <div class="ficon" role="img" aria-label="Icon of a cheering team" style="background:linear-gradient(135deg,#f9c2ab,#bcd2fa)"></div>
    <h3>Enim Ad Minima</h3>
    <p>Velit Esse Quam Nihil<br>Molestiae Conseq</p>
    <a>LEARN MORE</a>
  </div>
  <div class="abs feature" style="left:284px;top:1368px">
    <div class="ficon" role="img" aria-label="Icon of hands holding a group of people" style="background:linear-gradient(135deg,#bcd2fa,#f9c2ab)"></div>
    <h3>Corporis Suscipi</h3>
    <p>Velit Esse Quam Nihil<br>Molestiae Conseq</p>
    <a>LEARN MORE</a>
  </div>
  <div class="abs feature" style="left:52px;top:1608px">
    <div class="ficon" role="img" aria-label="Icon of a laughing face" style="background:linear-gradient(135deg,#f9c2ab,#bcd2fa)"></div>
    <h3>Deserunt Mollit</h3>
    <p>Velit Esse Quam Nihil<br>Molestiae Conseq</p>
    <a>LEARN MORE</a>
  </div>
  <div class="abs feature" style="left:288px;top:1608px">
    <div class="ficon" role="img" aria-label="Icon of a happy employee" style="background:linear-gradient(135deg,#bcd2fa,#f9c2ab)"></div>
    <h3>Cillum Dolore</h3>
    <p>Velit Esse Quam Nihil<br>Molestiae Conseq</p>
    <a>LEARN MORE</a>
  </div>

  <div class="abs video"></div>
  <div class="abs video-art" role="img" aria-label="Video illustration of an employee working on a laptop with message notifications"></div>
  <svg class="abs" style="left:912px;top:1558px" width="94" height="94" viewBox="0 0 94 94"><circle cx="47" cy="47" r="46" fill="#e0312b" opacity=".35"/><circle cx="47" cy="47" r="34" fill="#e0312b"/><polygon points="39,33 39,61 62,47" fill="#fff"/></svg>

  <!-- testimonial -->
  <div class="abs h2" style="left:0;top:1990px;width:1200px;text-align:center">TESTIMONIAL</div>
  <svg class="abs" style="left:572px;top:2028px" width="56" height="14" viewBox="0 0 56 14"><path d="M3 3Q28 20 53 3" fill="none" stroke="#f0501a" stroke-width="2.5" stroke-linecap="round"/></svg>

  <div class="abs avatar" role="img" aria-label="Portrait of a client" style="left:110px;top:2105px;width:90px;height:90px;background:linear-gradient(160deg,#8fb3d9,#d9b49b)"></div>
  <div class="abs avatar" role="img" aria-label="Portrait of a client" style="left:168px;top:2248px;width:70px;height:70px;background:linear-gradient(160deg,#cfcfcf,#6f6a66)"></div>
  <div class="abs avatar" role="img" aria-label="Portrait of a client" style="left:1000px;top:2105px;width:90px;height:90px;background:linear-gradient(160deg,#f2a66f,#5b4636)"></div>
  <div class="abs avatar" role="img" aria-label="Portrait of a client" style="left:965px;top:2248px;width:70px;height:70px;background:linear-gradient(160deg,#e4e4e4,#8a6a55)"></div>

  <div class="abs t-card"></div>
  <div class="abs avatar" role="img" aria-label="Portrait of the featured client" style="left:550px;top:2063px;width:100px;height:100px;background:linear-gradient(160deg,#e6e9ee,#b08b73);border:4px solid #fff"></div>
  <p class="abs t-text">Ut Enim Ad Minima Veniam, Quis Nostrum Exercitationem Ullam Corporis Suscipit Laboriosam, Nisi Ut Aliquid Ex Ea Commodi Consequatur? Quis Autem Vel Eum Iure Reprehenderit Qui In Ea Voluptate Velit Esse Quam Nihil Molestiae</p>
  <div class="abs t-divider"></div>
  <div class="abs quote" style="left:378px">“</div>
  <div class="abs quote" style="left:770px">”</div>
  <div class="abs t-name">Magna Aliqua - <small>HR management</small></div>
  <div class="abs stars">★★★★★</div>

  <!-- blog -->
  <div class="abs blog"></div>
  <div class="abs h2" style="left:0;top:2583px;width:1200px;text-align:center">BLOG</div>
  <svg class="abs" style="left:572px;top:2621px" width="56" height="14" viewBox="0 0 56 14"><path d="M3 3Q28 20 53 3" fill="none" stroke="#f0501a" stroke-width="2.5" stroke-linecap="round"/></svg>

  <svg class="abs" style="left:36px;top:2835px" width="28" height="44" viewBox="0 0 28 44"><path d="M24 3L5 22L24 41" fill="none" stroke="#111" stroke-width="5"/></svg>
  <svg class="abs" style="left:1134px;top:2835px" width="28" height="44" viewBox="0 0 28 44"><path d="M4 3L23 22L4 41" fill="none" stroke="#111" stroke-width="5"/></svg>

  <div class="abs post" style="left:105px">
    <div class="img" role="img" aria-label="Photo of a team joining hands in celebration" style="background:linear-gradient(150deg,#c9b49a,#8a5a44 55%,#3e3a3a)"></div>
    <span class="date">Jun 20, 2022</span>
    <h4>Ut Enim Ad Minima Veniam</h4>
    <p>Nemo Enim Ipsam Voluptatem Quia Voluptas Sit Aspernatur Aut Odit Aut Fugit, Sed Quia Consequ</p>
  </div>
  <div class="abs post" style="left:444px">
    <div class="img" role="img" aria-label="Photo of coworkers laughing together in an office" style="background:linear-gradient(150deg,#9fb0bd,#d9a23a 50%,#3b4a63)"></div>
    <span class="date">Jun 23, 2022</span>
    <h4>Inventore Veritatis Et</h4>
    <p>Nemo Enim Ipsam Voluptatem Quia Voluptas Sit Aspernatur Aut Odit Aut Fugit, Sed Quia Consequ</p>
  </div>
  <div class="abs post" style="left:785px">
    <div class="img" role="img" aria-label="Photo of a cheering group of colleagues" style="background:linear-gradient(150deg,#a9b6c4,#e3c7a8 50%,#8e3b3b)"></div>
    <span class="date">Jun 28, 2022</span>
    <h4>Magnam Aliquam Quaerat</h4>
    <p>Nemo Enim Ipsam Voluptatem Quia Voluptas Sit Aspernatur Aut Odit Aut Fugit, Sed Quia Consequ</p>
  </div>

  <!-- footer -->
  <svg class="abs" style="left:0;top:3140px" width="1200" height="438" viewBox="0 0 1200 438">
    <path d="M0 30C160 8 330 0 480 12C650 26 760 62 900 62C1020 62 1120 45 1200 30V438H0Z" fill="#f0501a"/>
    <path d="M0 45C160 22 330 15 480 28C650 44 760 82 900 82C1020 82 1120 62 1200 45V438H0Z" fill="#4a86f0"/>
  </svg>
  <div class="abs footer-name">velquo</div>

  <div class="abs fhead" style="left:437px">Quick Links</div>
  <div class="abs flinks">Home<br>About<br>Our Feature<br>Testimonial<br>Blog<br>Contact</div>

  <div class="abs fhead" style="left:622px">Sign up for our newsletter</div>
  <div class="abs email">Your Email Address</div>
  <div class="abs btn" style="left:624px;top:3385px;width:160px;height:42px;padding-left:32px;font-weight:500">SUBSCRIBE</div>

  <div class="abs fhead" style="left:965px">Follow us</div>
  <div class="abs social" style="left:966px"></div>
  <div class="abs social" style="left:1011px"></div>
  <div class="abs social" style="left:1055px"></div>

  <div class="abs fline"></div>
  <div class="abs copy">Copyrights@2022 Velquo. All Rights Reserved</div>

</div>
</body>
</html>
```